Pamphlet for introducing people to our church

I would like a church pamphlet designed, that includes the content in file "tovik-pamphlet.txt".

I am looking for a design that will incorporate the content in a professional and creative manner.

You do not have to use the content in any specific order, but I am relying on your skill and design knowledge to organize everything in an artistic and effective way.

Target Market(s)

Everyone

Industry/Entity Type

Religious

Requirements
Must have
• logo, use of content provided, use of branding (logo colors)
Nice to have
• More images where necessary
Should not have
• cross

```html
<!DOCTYPE html>
<html lang="en">
<head>
<meta charset="utf-8">
<title>TOVIK – Mission Statement Pamphlet</title>
<link rel="stylesheet" href="https://fonts.googleapis.com/css2?family=Anton&family=Montserrat:wght@400;500;600;700&display=swap">
<style>
  :root {
    --navy: #173a63;
    --orange: #f39321;
    --orange-deep: #ee7d1a;
    --text: #2b2f36;
    --paper: #ffffff;
    --backdrop: #e8e5e1;
  }
  * { box-sizing: border-box; margin: 0; padding: 0; }
  html, body { width: 1200px; height: 1200px; overflow: hidden; }
  body { background: var(--backdrop); font-family: "Montserrat", sans-serif; color: var(--text); }

  .pamphlet {
    position: absolute; left: 176px; top: 0;
    width: 848px; height: 1200px;
    background: var(--paper); overflow: hidden;
  }

  .flame-art {
    position: absolute; left: 575px; top: 250px; width: 273px; height: 840px;
    background: linear-gradient(160deg, #f7a43c 0%, var(--orange) 55%, var(--orange-deep) 100%);
    border-top-left-radius: 160px 320px;
  }

  .brand { position: absolute; left: 60px; top: 56px; display: flex; align-items: center; gap: 16px; }
  .brand-dot { width: 34px; height: 34px; border-radius: 50%; background: var(--orange); }
  .brand-name { font-size: 64px; font-weight: 600; color: var(--navy); letter-spacing: 2px; line-height: 1; }

  .headline { position: absolute; left: 60px; top: 152px; font-size: 44px; font-weight: 400; color: var(--navy); letter-spacing: 0.5px; }
  .section-title { position: absolute; left: 60px; top: 206px; font-family: "Anton", sans-serif; font-size: 62px; color: var(--orange); letter-spacing: 1px; line-height: 1; }

  .mission { position: absolute; left: 60px; top: 296px; width: 490px; font-size: 16px; line-height: 1.5; }
  .mission p + p { margin-top: 22px; }

  .ministries { position: absolute; left: 60px; top: 640px; width: 480px; font-size: 16px; line-height: 1.45; }
  .ministries-label { color: var(--orange); font-weight: 700; font-size: 16px; letter-spacing: 0.5px; }
  .ministry { margin-bottom: 16px; }
  .ministry-name { color: var(--navy); font-weight: 700; }

  .service { position: absolute; left: 60px; top: 900px; }
  .service-label { color: var(--orange); font-weight: 700; font-size: 21px; }
  .service-row { display: flex; align-items: center; gap: 16px; margin-top: 12px; }
  .service-time { font-size: 34px; font-weight: 600; color: var(--navy); }
  .service-place { font-size: 17px; font-weight: 600; color: var(--navy); line-height: 1.35; }

  .contact-band {
    position: absolute; left: 0; bottom: 0; width: 100%; height: 110px;
    background: var(--navy); color: #fff;
    display: flex; align-items: center; justify-content: space-around;
    font-size: 17px; font-weight: 500; padding: 0 30px;
  }
  .contact-item { display: flex; align-items: center; gap: 10px; }
</style>
</head>
<body>
  <main class="pamphlet">
    <div class="flame-art" role="img" aria-label="Large orange flame graphic"></div>

    <div class="brand">
      <span class="brand-dot"></span>
      <span class="brand-name">TOVIK</span>
    </div>

    <h1 class="headline">A VOICE TO THE NATIONS</h1>
    <h2 class="section-title">MISSION STATEMENT</h2>

    <section class="mission">
      <p>TOVIK is a gathering of believers whose purpose is to seek the face of God for an authentic restoration of the church as a body of born again believers around the world. As a gathering of believers, TOVIK seeks an awakening of the mind founded on the precepts and teachings of Jesus Christ.</p>
      <p>The modern church has replaced the simple and Kingdom centered principles of Jesus's disciples with complacent and compromised teachings on earthly prosperity. We believe in humbly seeking God without motive to use God or His Word for our own gain. The end times church will experience a glorious revival, renewed love and zeal for true discipleship, faith, and godliness as Jesus intended for us.</p>
    </section>

    <section class="ministries">
      <div class="ministries-label">MINISTRIES:</div>
      <div class="ministry"><span class="ministry-name">Kingdom seeds</span> (Children's ministry)<br>Children learn to be seeds of godliness in the world.</div>
      <div class="ministry"><span class="ministry-name">School of pilgrims</span><br>Learn the basics of Christian faith and about God's purpose for your life.</div>
      <div class="ministry"><span class="ministry-name">School of disciples</span><br>Deepen your knowledge of God's word and learn how to serve him.</div>
    </section>

    <section class="service">
      <div class="service-label">Sunday Service:</div>
      <div class="service-row">
        <svg width="44" height="44" viewBox="0 0 44 44" aria-hidden="true">
          <circle cx="22" cy="22" r="20" fill="#f39321"/>
          <circle cx="22" cy="22" r="14" fill="#fff" stroke="#173a63" stroke-width="2"/>
          <path d="M22 13v9l6 4" stroke="#173a63" stroke-width="2.4" fill="none" stroke-linecap="round"/>
        </svg>
        <span class="service-time">10:00am-12:30pm</span>
      </div>
      <div class="service-row">
        <svg width="44" height="30" viewBox="0 0 44 30" aria-hidden="true">
          <path d="M22 2c-5 0-9 4-9 9 0 7 9 16 9 16s9-9 9-16c0-5-4-9-9-9z" fill="none" stroke="#f39321" stroke-width="2.4"/>
          <circle cx="22" cy="11" r="3.2" fill="#f39321"/>
        </svg>
        <span class="service-place">Alder Community Hall<br>212 Maple Lane, Westbrook, ME 04092</span>
      </div>
    </section>

    <footer class="contact-band">
      <div class="contact-item">
        <svg width="22" height="22" viewBox="0 0 24 24" aria-hidden="true"><path d="M6.6 10.8a15 15 0 0 0 6.6 6.6l2.2-2.2a1 1 0 0 1 1-.25 11.4 11.4 0 0 0 3.6.57 1 1 0 0 1 1 1V20a1 1 0 0 1-1 1A17 17 0 0 1 3 4a1 1 0 0 1 1-1h3.5a1 1 0 0 1 1 1c0 1.25.2 2.45.57 3.6a1 1 0 0 1-.25 1z" fill="#f39321"/></svg>
        <span>(555) 014 2280</span>
      </div>
      <div class="contact-item">
        <svg width="24" height="18" viewBox="0 0 24 18" aria-hidden="true"><rect x="1" y="1" width="22" height="16" rx="1" fill="#f39321"/><path d="M1 1l11 9 11-9" stroke="#173a63" stroke-width="2" fill="none"/></svg>
        <span>contact@alderhollow.org</span>
      </div>
      <div class="contact-item">
        <svg width="22" height="22" viewBox="0 0 24 24" aria-hidden="true"><g fill="none" stroke="#f39321" stroke-width="2"><circle cx="12" cy="12" r="10"/><ellipse cx="12" cy="12" rx="4.5" ry="10"/><path d="M2 12h20M4 7h16M4 17h16"/></g></svg>
        <span>www.tovik.org</span>
      </div>
    </footer>
  </main>
</body>
</html>
```